Flyer-Design für Einzelhandel/Online-Shop für Werbetechnikzubehör
Zielgruppe
Wir sind ein Einzelhandel / Onlineshop für Werbetechnikzubehör. Plotterfolie, Plotter, DIY-Artikel. Wir kommen mitten aus dem Ruhrgebiet und unser Name verbindet das Plotten und unsere Herkunft. „Falzwerkstück“
Unsere Zielgruppe sind Kreative aus dem Bastel- / Nähbereich.
Aufgabenstellung
Wir legen wert auf die Verbindung zum Ruhrgebiet (Zechen und co.) Anbei stellen wir auch eine Datei zur Verfügung, die bereits auf unserem Auto und Gutscheinen implementiert ist. Gerne darf diese genutzt werden.
Wir legen Wert auf Gradlinigkeit und Übersichtlichkeit.
Unser Flyer soll ein A6 Format sein (Datenformat: 154 x 111 mm
3 mm Beschnitt) diesen wir mit einem Rabattcode versehen wollen.
Des Weiteren benötigen wir auch die Abbidung von Instagram / Facebook / Homepage.
Daher benötigen wir das Design natürlich auch in einem Bearbeitungsmodus für ai.
Gerade die Felder Rabattcode und Gutscheinbedingungen sollten beachtet werden.
10% auf alle Vinyl, Flex & Flockfolie (Bogenware)
Der Flyer wird als Versandbeileger für befreundete Unternehmen benötigt.
Wir möchten mit diesem Flyer Neukunden gewinnen.
Der Flyer kann beidseitig gestaltet werden. Hoch oder Quer ist auch frei wählbar.
Unsere Farben sind als Datei hochgeladen.

```html
<!DOCTYPE html>
<html lang="de">
<head>
<meta charset="utf-8">
<title>Falzwerkstück – Neukundenrabatt Flyer</title>
<link href="https://fonts.googleapis.com/css2?family=Barlow+Condensed:wght@300;400;500;600;700&display=swap" rel="stylesheet">
<style>
  :root{
    --teal:#5199a8;
    --teal-line:#4f97a6;
    --ink:#555657;
    --ink-dark:#3f4041;
    --skyline:#5a5a5b;
    --skyline-faint:#dcdcdc;
    --paper:#ffffff;
    --page:#f4f4f4;
  }
  *{margin:0;padding:0;box-sizing:border-box}
  html,body{width:1140px;height:1200px;overflow:hidden;background:var(--page)}
  body{font-family:"Barlow Condensed",Arial Narrow,sans-serif;color:var(--ink);position:relative}
  .card{position:absolute;left:180px;width:780px;height:554px;background:var(--paper);box-shadow:0 1px 6px rgba(0,0,0,.22)}
  .card--front{top:32px}
  .card--back{top:614px}

  /* front */
  .skyline{position:absolute;left:0;top:40px;width:780px;height:122px;background:linear-gradient(180deg,rgba(90,90,91,.15),var(--skyline) 85%)}
  .ground-line{position:absolute;left:0;top:167px;width:780px;height:4px;background:var(--skyline)}
  .band{position:absolute;left:0;top:179px;width:780px;height:98px;background:var(--teal);display:flex;align-items:center;justify-content:center}
  .headline{font-size:54px;font-weight:400;letter-spacing:2px;color:#fff;line-height:1}
  .headline b{font-weight:700}
  .brand-front{position:absolute;left:0;width:780px;top:400px;text-align:center;font-size:46px;font-weight:400;letter-spacing:1px;color:var(--ink);text-transform:uppercase}

  /* back */
  .skyline--faint{position:absolute;left:246px;top:30px;width:487px;height:88px;background:linear-gradient(180deg,rgba(220,220,220,.3),var(--skyline-faint) 80%)}
  .rule{position:absolute;left:49px;top:122px;width:684px;height:3px;background:var(--teal-line)}
  .brand-back{position:absolute;left:49px;top:86px;font-size:24px;font-weight:500;color:var(--teal);text-transform:uppercase;letter-spacing:1px}
  .back-title{position:absolute;right:47px;top:170px;font-size:42px;font-weight:400;color:var(--ink);letter-spacing:1px;line-height:1}
  .back-title b{font-weight:700}
  .field{position:absolute;top:242px}
  .field--valid{left:49px;width:293px}
  .field--code{left:438px;width:295px}
  .field-label{font-size:20px;font-weight:600;color:var(--teal);line-height:1}
  .field-line{margin-top:34px;height:1.5px;background:var(--teal-line)}
  .conditions{position:absolute;left:49px;top:338px;width:686px;font-size:14.5px;line-height:18.6px;color:var(--ink-dark);font-weight:400}
  .conditions strong{font-weight:700}
  .footer{position:absolute;right:47px;top:498px;font-size:17px;font-weight:400;color:var(--ink);display:flex;align-items:center;gap:10px;white-space:nowrap}
  .footer .sep{color:var(--ink)}
  .footer .url{color:var(--teal);font-weight:600}
  .footer .name{text-transform:uppercase}
  .footer .social{color:var(--ink-dark);font-weight:600;margin-left:8px}
</style>
</head>
<body>
  <section class="card card--front">
    <div class="skyline" role="img" aria-label="Silhouette der Ruhrgebiets-Skyline mit Fördertürmen, Halde, Windrad und Fernsehturm"></div>
    <div class="ground-line"></div>
    <div class="band"><h1 class="headline">NEUKUNDEN<b>RABATT</b></h1></div>
    <div class="brand-front">Falzwerkstück</div>
  </section>

  <section class="card card--back">
    <div class="skyline--faint" role="img" aria-label="Blasse Silhouette der Ruhrgebiets-Skyline"></div>
    <div class="brand-back">Falzwerkstück</div>
    <div class="rule"></div>
    <h2 class="back-title">NEUKUNDEN<b>RABATT</b></h2>
    <div class="field field--valid"><div class="field-label">GÜLTIG BIS</div><div class="field-line"></div></div>
    <div class="field field--code"><div class="field-label">RABATT-CODE</div><div class="field-line"></div></div>
    <p class="conditions"><strong>BEDINGUNGEN:</strong> Lorem ipsum dolor sit amet, consectetuer adipiscing elit, sed diam nonummy nibh euismod incidunt ut laoreet dolore magna aliquam erat volutpat.<br>Ut wisi enim ad minim veniam, quis nostrud exercitation ullamcorper suscipit lobortis nisl ut aliquip ex ea commodo consequat. Duis autem vel eum iriure dolor in.</p>
    <div class="footer">
      <span class="name">Falzwerkstück</span><span class="sep">|</span>
      <span>Zechenweg 12</span><span class="sep">|</span>
      <span>45127 Essen</span><span class="sep">|</span>
      <span class="url">www.falzwerkstueck.de</span>
      <span class="social">@falzwerkstueck</span>
    </div>
  </section>
</body>
</html>
```